Tideward Fuel Product design

We need a bottle design for our product. Tideward Fuel is a Gaming Nootropic made to increase Energy, Focus, Reaction time, and Clarity of an eSport gamer. It will be 40 servings a bottle. Currently, all the ingredients haven't been finalized so after the competition is over we will have to work with the designer to also make an ingredients label for the back of it. For the flavor, we will call it ember dusk.

The attachments included:. The velvet mongoose picture as a font style I like for the logo.
The K BOLT SURGEWAVE PICTURE IS WHAT WE WANT OUR DESIGN to look like something similar a clean and simple design that stands out!

K Bolt bottle is what our biggest competitors product looks like. The tideward fuel picture as the current logo we are using but can be changed.

Overall the pictures are just some references for what I could possibly want the design to look like however, I'm open to your designer's ideas and concepts you think would make for a cool looking Gaming Nootropic product bottle design. I appreciate everyone working on this and look forward to seeing your designs have a great day!

Target Market(s)

Gamers between the ages of 18-30

Industry/Entity Type

Health And Wellness

Requirements
Must have
• Tideward Fuel logo, state that it is for energy, focus, reaction, and clarity. state 40 serivngs. state flavor.

```html
<!DOCTYPE html>
<html lang="en">
<head>
<meta charset="utf-8">
<title>Tideward Fuel – Ember Dusk Label</title>
<link rel="stylesheet" href="https://fonts.googleapis.com/css2?family=Barlow+Condensed:ital,wght@0,600;0,700;1,600;1,700&display=swap">
<style>
  :root {
    --page: #f3f4f6;
    --haze-top: #cfe2f2;
    --haze-mid: #f4f8fc;
    --white: #ffffff;
    --deep-band: #1d5b9f;
    --deep-tab: #2a6fb5;
    --deep-ink: #1f62ab;
    --sky-band: #2a87c2;
    --sky-tab: #3796cf;
    --sky-ink: #2786c4;
    --peak-light: #e8f1f9;
    --peak-shade: #6f9bc8;
  }
  * { margin: 0; padding: 0; box-sizing: border-box; }
  html, body {
    width: 1200px; height: 1200px; overflow: hidden;
    background: var(--page);
    font-family: "Barlow Condensed", "Arial Narrow", sans-serif;
  }
  .canvas {
    width: 1200px; height: 1200px;
    display: flex; flex-direction: column; justify-content: center; align-items: center;
    gap: 60px;
  }
  .label {
    --band: var(--deep-band);
    --tab: var(--deep-tab);
    --ink: var(--deep-ink);
    position: relative;
    width: 1080px; height: 500px;
    overflow: hidden;
    background: linear-gradient(180deg, var(--haze-top) 0%, var(--haze-mid) 30%, var(--white) 48%, var(--haze-mid) 62%, #dce9f5 100%);
    box-shadow: 0 10px 30px rgba(30, 60, 100, 0.12);
  }
  .label--sky {
    --band: var(--sky-band);
    --tab: var(--sky-tab);
    --ink: var(--sky-ink);
  }
  .servings-badge {
    position: absolute; top: 26px; right: 40px;
    width: 96px; height: 100px;
    background: var(--ink);
    border-radius: 0 0 0 18px;
    color: var(--white);
    display: flex; flex-direction: column; align-items: center; justify-content: center;
    line-height: 1;
  }
  .servings-badge .count { font-size: 52px; font-weight: 700; }
  .servings-badge .unit { font-size: 17px; font-weight: 600; letter-spacing: 0.5px; }
  .brand {
    position: absolute; top: 70px; left: 0; right: 0;
    display: flex; align-items: center; justify-content: center; gap: 12px;
  }
  .brand-dot {
    width: 34px; height: 34px; border-radius: 50%;
    background: var(--ink);
  }
  .brand-name {
    font-size: 34px; font-weight: 700; color: var(--ink);
    text-transform: uppercase; letter-spacing: 1px;
  }
  .flavor-title {
    position: absolute; top: 140px; left: 0; right: 0;
    text-align: center;
    font-size: 118px; font-weight: 700; font-style: italic;
    color: var(--ink); letter-spacing: 1px; line-height: 1;
  }
  .benefit-band {
    position: absolute; left: 0; right: 0; bottom: 0; height: 190px;
    background: var(--band);
  }
  .benefit-tab {
    position: absolute; left: 50%; top: 292px;
    transform: translateX(-50%);
    width: 700px; height: 64px;
    background: var(--tab);
    clip-path: polygon(3% 0, 97% 0, 100% 100%, 0 100%);
    display: flex; align-items: center; justify-content: center;
  }
  .benefits {
    color: var(--white);
    font-size: 40px; font-weight: 600; font-style: italic;
    letter-spacing: 0.5px; white-space: nowrap;
  }
  .benefits .sep { margin: 0 8px; }
  .peak-art {
    position: absolute; left: 50%; bottom: 0;
    transform: translateX(-50%);
    width: 440px; height: 120px;
    border-radius: 200px 200px 0 0;
    background: radial-gradient(ellipse at 50% 30%, var(--peak-light) 0%, var(--peak-shade) 75%, var(--band) 100%);
  }
</style>
</head>
<body>
<main class="canvas">
  <section class="label label--deep">
    <div class="servings-badge"><span class="count">40</span><span class="unit">servings</span></div>
    <div class="brand"><span class="brand-dot"></span><span class="brand-name">Tideward Fuel</span></div>
    <h1 class="flavor-title">EMBER DUSK</h1>
    <div class="benefit-band"></div>
    <div class="benefit-tab">
      <p class="benefits">energy<span class="sep">•</span>focus<span class="sep">•</span>reaction<span class="sep">•</span>clarity</p>
    </div>
    <div class="peak-art" role="img" aria-label="Snowy mountain range illustration"></div>
  </section>

  <section class="label label--sky">
    <div class="servings-badge"><span class="count">40</span><span class="unit">servings</span></div>
    <div class="brand"><span class="brand-dot"></span><span class="brand-name">Tideward Fuel</span></div>
    <h2 class="flavor-title">EMBER DUSK</h2>
    <div class="benefit-band"></div>
    <div class="benefit-tab">
      <p class="benefits">energy<span class="sep">•</span>focus<span class="sep">•</span>reaction<span class="sep">•</span>clarity</p>
    </div>
    <div class="peak-art" role="img" aria-label="Snowy mountain range illustration"></div>
  </section>
</main>
</body>
</html>
```